Mobile Friendly Lead Generation Landing Page

We are a web marketing company that specialized in web lead generation. Recently we have started buying media from mobile devices and we need a mobile interface(landing page) where we can collect user data in an effective manner.

Our current mobile landing page is:
http://www.pathwaylocate.example.com/lp13d/index.aspx?a=true&source=591483
Through this you can see what the steps/questions users need to answer to get matched to a school. We need the design for the whole process.

We are pretty open for design ideas and our goal is to make this mobile optimized landing page have the look and feel of an app...but not an app.
There are several questions in the process but we are open to changing the way they are presented. As in, you can have one question at a time or a few.
The goal is to make this EXTREMELY EASY for users to interact with.

One example that we have liked is:
http://tutorhubnet.example.com/schools/72615-page1.thub (please note that this opens only on mobile devices)

Some of these screenshots are attached.

Our web form looks like this:
http://www.pathwaylocate.example.com/lp88/index.aspx?a=true

```html
<!DOCTYPE html>
<html lang="en">
<head>
<meta charset="utf-8">
<title>PathwayLocate – Get Matched</title>
<link rel="stylesheet" href="https://fonts.googleapis.com/css2?family=Roboto:wght@300;400;500&display=swap">
<style>
  :root {
    --canvas-bg: #eceff3;
    --page-bg: #ffffff;
    --banner-top: #f6efe2;
    --banner-mid: #f3e6cf;
    --banner-band: #efe2c8;
    --ink: #2b2b2b;
    --ink-soft: #555555;
    --accent: #1a8fe3;
    --accent-dark: #0f77c9;
    --track: #dfe4ea;
    --field-bg: #f4f4f4;
    --field-line: #e4e4e4;
    --placeholder: #a9a9a9;
    --fine-print: #b3b3b3;
    --logo-ink: #3e4a1f;
    --button-bg: #efefef;
    --button-line: #c9c9c9;
    --button-ink: #555555;
  }
  * { box-sizing: border-box; margin: 0; padding: 0; }
  html, body {
    width: 1200px; height: 2773px; overflow: hidden;
    background: var(--canvas-bg);
    font-family: "Roboto", "Helvetica Neue", Arial, sans-serif;
  }
  .page {
    position: absolute; left: 0; top: 535px;
    width: 1200px; height: 1702px;
    background: var(--page-bg);
  }
  .hero {
    position: absolute; left: 0; top: 0; width: 1200px; height: 272px;
    background: linear-gradient(100deg, var(--banner-top) 0%, var(--banner-mid) 55%, #e9dcc8 100%);
  }
  .hero-band {
    position: absolute; left: 0; top: 148px; width: 1200px; height: 124px;
    background: linear-gradient(90deg, rgba(239,226,200,.9), rgba(233,222,205,.7));
  }
  .brand {
    position: absolute; left: 0; top: 40px; width: 1200px;
    display: flex; justify-content: center; align-items: center; gap: 14px;
  }
  .brand-dot { width: 22px; height: 22px; border-radius: 50%; background: var(--logo-ink); }
  .brand-name { font-size: 52px; font-weight: 500; color: var(--logo-ink); letter-spacing: -0.5px; }
  .tagline {
    position: absolute; left: 0; top: 172px; width: 1200px;
    display: flex; justify-content: center; align-items: baseline; gap: 16px;
    white-space: nowrap;
  }
  .tagline-lead { font-size: 45px; font-weight: 400; color: var(--ink); letter-spacing: -1px; }
  .tagline-body { font-size: 54px; font-weight: 300; color: var(--ink-soft); letter-spacing: -1px; }
  .tagline-now { font-size: 66px; font-weight: 400; color: var(--accent); }
  .progress {
    position: absolute; left: 22px; top: 380px; width: 1156px; height: 31px;
    background: var(--track); border-radius: 8px; overflow: hidden;
  }
  .progress-fill {
    width: 780px; height: 100%; border-radius: 8px;
    background: linear-gradient(180deg, var(--accent), var(--accent-dark));
  }
  .form-title {
    position: absolute; left: 22px; top: 474px;
    font-size: 54px; font-weight: 400; color: var(--ink-soft);
  }
  .field {
    position: absolute; left: 22px; width: 1160px; height: 128px;
    background: var(--field-bg); border: 2px solid var(--field-line); border-radius: 4px;
    display: flex; align-items: center; padding-left: 34px;
    font-size: 48px; font-weight: 300; color: var(--placeholder);
  }
  .field-select { padding-right: 0; }
  .select-arrow {
    position: absolute; right: 0; top: 0; width: 128px; height: 124px;
    border-left: 2px solid var(--field-line);
    display: flex; align-items: center; justify-content: center;
  }
  .consent {
    position: absolute; left: 22px; top: 1350px; width: 1160px;
    display: flex; gap: 20px;
  }
  .consent-box {
    flex: none; width: 30px; height: 30px; margin-top: 4px;
    border: 2px solid #c4c4c4; border-radius: 4px; background: #fafafa;
  }
  .consent-text { font-size: 27px; line-height: 1.25; color: var(--fine-print); letter-spacing: -0.3px; }
  .next-button {
    position: absolute; left: 535px; top: 1529px; width: 128px; height: 128px;
    border-radius: 50%; background: var(--button-bg); border: 3px solid var(--button-line);
    display: flex; align-items: center; justify-content: center;
  }
</style>
</head>
<body>
  <main class="page">
    <header class="hero" role="img" aria-label="Soft blurred campus photo behind the brand banner">
      <div class="hero-band"></div>
      <div class="brand">
        <span class="brand-dot"></span>
        <span class="brand-name">PathwayLocate</span>
      </div>
      <div class="tagline">
        <span class="tagline-lead">GET MATCHED TO</span>
        <span class="tagline-body">Online &amp; Local Colleges</span>
        <span class="tagline-now">Now!</span>
      </div>
    </header>

    <div class="progress"><div class="progress-fill"></div></div>

    <h1 class="form-title">Your Personal Information:</h1>

    <div class="field" style="top:594px">Zip Code</div>
    <div class="field" style="top:747px">Address</div>
    <div class="field" style="top:895px">Suite/Apt.#</div>
    <div class="field" style="top:1045px">City</div>
    <div class="field field-select" style="top:1196px">Please Slect State
      <span class="select-arrow">
        <svg width="40" height="24" viewBox="0 0 40 24"><polyline points="4,5 20,19 36,5" fill="none" stroke="#c9c9c9" stroke-width="5" stroke-linecap="round" stroke-linejoin="round"/></svg>
      </span>
    </div>

    <div class="consent">
      <span class="consent-box"></span>
      <p class="consent-text">Checking this box is required for PathwayLocate.example.com and/or degreepathway.example.org to contact me, without obligation to attend the University. I understand that I will not be obligated to provide consent in order to receive or purchase services from any University.</p>
    </div>

    <div class="next-button" aria-label="Next step">
      <svg width="40" height="44" viewBox="0 0 40 44"><polygon points="8,4 36,22 8,40" fill="var(--button-ink)"/></svg>
    </div>
  </main>
</body>
</html>
```